CaptainKettle needs a new packaging

We are Coffee Roasters based in Versailles France.

We want a new design for our coffee packaging. The packaging is a basic brown paper bag. We are sticking on it a 99.1mm x 67.7mm Label.

We want a new design for the label. The label should have the following info : Name of the coffee, origin, one line of description, our website www.captainkettle.fr.

Enclosed you will find our logo, as well as a picture of our current packaging

The Design should be "simple yet sophisticate".

```html
<!DOCTYPE html>
<html lang="fr">
<head>
<meta charset="utf-8">
<title>CaptainKettle – Coffee Label Nº5</title>
<link rel="stylesheet" href="https://fonts.googleapis.com/css2?family=Libre+Baskerville:ital,wght@0,400;0,700;1,400&display=swap">
<style>
  :root {
    --ink: #231f20;
    --paper: #ffffff;
    --pattern-light: #f6f6f6;
    --pattern-mid: #ececec;
    --dot: #2a2a2a;
  }
  html, body {
    margin: 0;
    padding: 0;
    width: 1200px;
    height: 820px;
    overflow: hidden;
    background: var(--paper);
  }
  .label {
    position: relative;
    width: 1200px;
    height: 820px;
    overflow: hidden;
    color: var(--ink);
    font-family: "Libre Baskerville", "Century Schoolbook", Georgia, serif;
  }
  .bean-pattern {
    position: absolute;
    inset: 0;
    background: radial-gradient(ellipse at center, var(--pattern-light) 0%, var(--pattern-mid) 100%);
  }
  .frame {
    position: absolute;
    inset: 0;
  }
  .brand-mark {
    position: absolute;
    left: 270px;
    top: 110px;
  }
  .brand-name {
    position: absolute;
    left: 428px;
    top: 148px;
    margin: 0;
    font-size: 62px;
    line-height: 1;
    font-weight: 700;
    white-space: nowrap;
  }
  .brand-tagline {
    position: absolute;
    left: 430px;
    top: 230px;
    margin: 0;
    font-size: 28px;
    line-height: 1;
    font-weight: 400;
    white-space: nowrap;
  }
  .centered {
    position: absolute;
    left: 0;
    width: 1200px;
    margin: 0;
    text-align: center;
    line-height: 1;
    white-space: nowrap;
  }
  .coffee-name {
    top: 348px;
    font-size: 70px;
    font-weight: 700;
  }
  .coffee-name sup {
    font-size: 0.55em;
    vertical-align: 0.7em;
    line-height: 0;
  }
  .coffee-type {
    top: 434px;
    font-size: 28px;
    font-weight: 700;
  }
  .coffee-origin {
    top: 483px;
    font-size: 31px;
    font-weight: 700;
  }
  .coffee-description {
    top: 551px;
    font-size: 25px;
    font-style: italic;
    font-weight: 400;
  }
  .website {
    top: 647px;
    font-size: 58px;
    font-weight: 700;
  }
</style>
</head>
<body>
  <main class="label">
    <div class="bean-pattern" role="img" aria-label="Soft repeating pattern of outlined coffee beans in light grey"></div>

    <svg class="frame" width="1200" height="820" viewBox="0 0 1200 820" aria-hidden="true">
      <rect x="40" y="38" width="1122" height="742" fill="none" stroke="var(--dot)" stroke-width="3" stroke-linecap="round" stroke-dasharray="0 7.5"/>
    </svg>

    <svg class="brand-mark" width="140" height="140" viewBox="0 0 140 140" aria-hidden="true">
      <circle cx="70" cy="70" r="68" fill="var(--ink)"/>
    </svg>
    <p class="brand-name">CaptainKettle</p>
    <p class="brand-tagline">Artisan Torréfacteur</p>

    <h1 class="centered coffee-name">N<sup>o</sup>5 de CaptainKettle</h1>
    <p class="centered coffee-type">100% Arabica</p>
    <p class="centered coffee-origin">(Bresil, Congo, Ethipie)</p>
    <p class="centered coffee-description">One line text goes here, lorem ipsum doler amit</p>
    <p class="centered website">www.captainkettle.fr</p>
  </main>
</body>
</html>
```